We want our 2017 Velmar Oskin Hauler 350 Van Medium Roof 148 WB to POP

We are a lawn and property management company that specializes in lawn care; mowing, fertilizing, weed control, seasonal clean up, and full Property Management; interior and exterior cleaning, maintenence , and more.
Our vans are white and we do not want to full body wraps. Just strategically placed decals.
Simple, minimalist design without a lot of fuss or detail.

Local community members. Residential and Commercial

Lawn and Property Management

• Phone number: 715-555-0193 website: www.bramwickyard.example
• Cartoon characters or loud, obnoxious graphics

```html
<!DOCTYPE html>
<html lang="en">
<head>
<meta charset="utf-8">
<title>Bramwick Yard – Van Decal Layouts</title>
<link rel="stylesheet" href="https://fonts.googleapis.com/css2?family=Montserrat:wght@600;700&display=swap">
<style>
  :root {
    --canvas: #ffffff;
    --panel-edge: #d9dcd6;
    --panel-white: #f7f8f6;
    --green-deep: #1e7d2c;
    --green-mid: #3a9a2a;
    --green-lime: #7cc423;
    --purple: #8a25b8;
    --ink: #1d1d1b;
    --text-light: #ffffff;
  }
  html, body {
    margin: 0;
    padding: 0;
    width: 1200px;
    height: 1200px;
    overflow: hidden;
    background: var(--canvas);
    font-family: "Montserrat", Arial, sans-serif;
  }
  .sheet {
    width: 1200px;
    height: 1200px;
    display: flex;
    flex-direction: column;
    justify-content: space-around;
    align-items: center;
    padding: 60px 0;
    box-sizing: border-box;
  }
  .decal-layout {
    width: 1080px;
    height: 420px;
    display: block;
  }
  .body-outline { fill: var(--panel-white); stroke: var(--panel-edge); stroke-width: 2; }
  .brand-name { font-family: "Montserrat", Arial, sans-serif; font-weight: 700; font-size: 40px; fill: var(--ink); }
  .brand-dot { fill: var(--green-mid); }
  .phone { font-family: "Montserrat", Arial, sans-serif; font-weight: 700; font-size: 34px; letter-spacing: 2px; }
  .web { font-family: "Montserrat", Arial, sans-serif; font-weight: 600; font-size: 19px; }
  .phone--light, .web--light { fill: var(--text-light); }
  .phone--green { fill: var(--green-deep); }
  .web--purple { fill: var(--purple); }
  .swoosh { fill: none; stroke: var(--purple); stroke-linecap: round; }
  .swoosh-highlight { fill: none; stroke: #ffffff; }
  .rocker-stripe { fill: var(--green-lime); }
</style>
</head>
<body>
<main class="sheet">

  <svg class="decal-layout" viewBox="0 0 1080 420" role="img" aria-label="Side decal layout with green rear sweep">
    <defs>
      <clipPath id="bodyA">
        <path d="M0,420 L0,175 C20,125 120,45 210,12 Q230,4 260,4 L1060,0 Q1080,0 1080,20 L1080,420 Z"/>
      </clipPath>
      <linearGradient id="sweepA" x1="0" y1="1" x2="1" y2="0">
        <stop offset="0" stop-color="var(--green-lime)"/>
        <stop offset="0.55" stop-color="var(--green-mid)"/>
        <stop offset="1" stop-color="var(--green-deep)"/>
      </linearGradient>
    </defs>
    <path class="body-outline" d="M0,420 L0,175 C20,125 120,45 210,12 Q230,4 260,4 L1060,0 Q1080,0 1080,20 L1080,420 Z"/>
    <g clip-path="url(#bodyA)">
      <path fill="url(#sweepA)" d="M330,332 C550,312 710,240 805,140 C865,78 900,30 925,0 L1080,0 L1080,420 L330,420 Z"/>
      <path class="swoosh-highlight" stroke-width="6" d="M300,328 C535,308 695,236 792,134 C852,72 888,26 914,0"/>
      <path class="swoosh" stroke-width="10" d="M280,322 C520,300 680,230 780,130 C840,70 880,25 905,-4"/>
      <rect class="rocker-stripe" x="300" y="372" width="780" height="14"/>
    </g>
    <circle class="brand-dot" cx="284" cy="176" r="11"/>
    <text class="brand-name" x="304" y="190">Bramwick Yard</text>
    <text class="phone phone--light" x="770" y="240">715-555-0193</text>
    <text class="web web--light" x="772" y="274">www.bramwickyard.example</text>
  </svg>

  <svg class="decal-layout" viewBox="0 0 1080 420" role="img" aria-label="Side decal layout with green lower band">
    <defs>
      <clipPath id="bodyB">
        <path d="M0,420 L0,175 C20,125 120,45 210,12 Q230,4 260,4 L1060,0 Q1080,0 1080,20 L1080,420 Z"/>
      </clipPath>
      <linearGradient id="bandB" x1="0" y1="0" x2="1" y2="0">
        <stop offset="0" stop-color="var(--green-lime)"/>
        <stop offset="0.6" stop-color="var(--green-mid)"/>
        <stop offset="1" stop-color="var(--green-deep)"/>
      </linearGradient>
    </defs>
    <path class="body-outline" d="M0,420 L0,175 C20,125 120,45 210,12 Q230,4 260,4 L1060,0 Q1080,0 1080,20 L1080,420 Z"/>
    <g clip-path="url(#bodyB)">
      <path fill="url(#bandB)" d="M0,318 C260,300 600,262 1080,250 L1080,420 L0,420 Z"/>
      <path class="swoosh-highlight" stroke-width="6" d="M0,304 C280,288 600,252 1080,238"/>
      <path class="swoosh" stroke-width="12" d="M0,292 C280,276 600,240 1080,224"/>
      <rect class="rocker-stripe" x="300" y="372" width="780" height="14"/>
    </g>
    <circle class="brand-dot" cx="284" cy="176" r="11"/>
    <text class="brand-name" x="304" y="190">Bramwick Yard</text>
    <text class="phone phone--green" x="740" y="110">715-555-0193</text>
    <text class="web web--purple" x="742" y="144">www.bramwickyard.example</text>
  </svg>

</main>
</body>
</html>
```